New website for selling opensource software business to business

Website K7 Software

The open source software industry has grown enormously in recent years. More and more customers from software companies choose an open source solution. K7 Software is going to fulfill this increasing demand.

Core business

Reselling software subcriptions (business to business).

Side business

Selling consultancy and Training to customers

Goals:

- Binding of customers to K7 IT Group
- Sales of subscriptions to customer
- Enlarge network K7 IT Group
- USP: Sales of complete package, Software, consultancy and training

Products

There are a couple of products/ services that K7 will provide. Below you will find an overview of the Products:

- Bluefox subscriptions
- Crater subscriptions
- Velmor products
- Customized consultancy for the customer
- Customized training for the customer

Style

Behind the website should be a cms system like pagecraft.

Target Market(s)

Business - Business

Industry/Entity Type

Business

Coding

Coded - Design and coding required

Number of Pages Required

5+ page

Font styles to use
Other font styles liked:
• Calibri

Colors
0355a3
3176b5
85abd2

Requirements
Must have
• Home page with large photo background, About us, contact page with safe option to request more info
• Portfolio pages:
• 4 pages with a product group each:
• 1. Blue fox
• 2. Craters
• 3. Velmor
• 4. Ourtrustwall
• 1. Blue Fox
• On top space for short info/bullets about Blue fox. Further, a grid with 8 columns. In the columns 2 buttons both lead to a popup. A popup for information and a popup for requesting a quote.
• 2. Crater:
• On top space for short info/bullets about Crater. Further, a grid with 3 columns. In the columns 2 buttons both lead to a popup. A popup for information and a popup for requesting a quote.
• 1. Velmor:
• On top space for short info/bullets about Velmor. Further, a grid with 4 columns. In the columns 2 buttons both lead to a popup. A popup for information and a popup for requesting a quote.
• 2. Ourtrustwall:
• On top space for short info/bullets about Ourtrustwall. Further, a grid with 2 columns. In the columns 2 buttons both lead to a popup. A popup for information and a popup for requesting a quote.

```html
<!DOCTYPE html>
<html lang="en">
<head>
<meta charset="utf-8">
<title>K7 Software</title>
<link rel="stylesheet" href="https://fonts.googleapis.com/css2?family=Open+Sans:wght@400;600;700&display=swap">
<style>
:root{
  --brand:#0355a3;
  --brand-mid:#3176b5;
  --brand-light:#85abd2;
  --ink:#222;
  --muted:#666;
  --line:#d6d6d6;
  --band:#f1f1f1;
  --footer:#333;
  --white:#fff;
}
*{box-sizing:border-box;margin:0;padding:0}
html,body{width:717px;height:1200px;overflow:hidden}
body{position:relative;font-family:"Open Sans",Arial,sans-serif;color:var(--ink);background:var(--white)}
.abs{position:absolute;white-space:nowrap}
a{color:inherit;text-decoration:none}

/* header */
.site-header{position:absolute;left:0;top:0;width:717px;height:107px;background:var(--white)}
.brand-mark{left:79px;top:14px;width:80px;height:80px;border-radius:50%;background:#ececef;display:flex;align-items:center;justify-content:center;font-weight:700;font-size:26px;color:var(--brand)}
.contact-mail{right:176px;top:24px;font-size:11px;line-height:14px;color:var(--ink);display:flex;align-items:center;gap:6px}
.quick-contact{left:552px;top:20px;width:85px;height:23px;background:var(--brand);color:var(--white);font-size:8px;font-weight:700;display:flex;align-items:center;justify-content:center;gap:4px;letter-spacing:.2px}
.main-nav{top:61px;font-size:8.5px;font-weight:600;color:var(--ink)}
.main-nav.active{color:var(--brand)}

/* hero */
.hero{left:0;top:107px;width:717px;height:259px;background:linear-gradient(100deg,#3a3d44 0%,#4c5058 45%,#2c2f35 75%,#6e7278 100%)}
.hero-title{left:80px;top:217px;color:var(--white);font-size:15px;font-weight:700;line-height:1.2}
.hero-sub{left:80px;top:235px;color:var(--white);font-size:15px;font-weight:400}
.hero-btn{left:79px;top:261px;width:58px;height:23px;background:var(--white);font-size:7.5px;display:flex;align-items:center;justify-content:center;color:var(--ink)}
.hero-arrow{top:230px}

/* welcome */
.welcome{left:0;top:366px;width:717px;height:148px;background:var(--band)}
.section-title{left:0;width:717px;text-align:center;color:var(--brand);font-weight:700;font-size:14px}
.welcome-text{left:78px;top:433px;width:561px;text-align:center;font-size:7.1px;line-height:11.6px;color:#444;white-space:normal}

/* products */
.product{width:130px}
.product-logo{width:130px;height:71px;background:var(--band);display:flex;align-items:center;justify-content:center;gap:6px;font-size:16px;font-weight:600;color:var(--ink)}
.product-dot{width:14px;height:14px;border-radius:50%;background:var(--brand)}
.product-name{text-align:center;font-size:10px;color:#444;margin-top:5px}
.read-more{margin:3px auto 0;width:49px;height:20px;border:1px solid #ccc;font-size:6.2px;color:#888;display:flex;align-items:center;justify-content:center}
.divider{left:79px;top:736px;width:558px;height:1px;background:#e2e2e2}

/* blog */
.post{width:176px;height:247px;border:1px solid var(--line);background:var(--white);white-space:normal}
.post-media{width:174px;height:104px}
.post-body{padding:14px 13px 0 14px}
.post-title{font-size:9.5px;line-height:13.5px;color:var(--ink);font-weight:400}
.post-date{margin-top:11px;font-size:6.6px;color:var(--brand)}
.post-excerpt{margin-top:10px;font-size:6.2px;line-height:10.5px;color:var(--muted)}
.post-excerpt span{color:var(--ink);text-decoration:underline}
.view-all{left:330px;top:1081px;width:57px;height:23px;border:1px solid #ccc;font-size:7.5px;color:#888;display:flex;align-items:center;justify-content:center}

/* footer */
.site-footer{left:0;top:1142px;width:717px;height:58px;background:var(--footer)}
.footer-nav{left:79px;top:1157px;font-size:6.8px;color:#ddd}
.footer-copy{left:79px;top:1174px;font-size:6.8px;color:#ccc}
.social{top:1163px;width:16px;height:16px;border-radius:50%}
</style>
</head>
<body>

<header class="site-header">
  <div class="abs brand-mark">K7</div>
  <div class="abs contact-mail">
    <svg width="10" height="8" viewBox="0 0 10 8"><rect x="0" y="0" width="10" height="8" fill="#222"/><path d="M0 0 L5 4.5 L10 0" stroke="#fff" stroke-width="1" fill="none"/></svg>
    <span>info@k7software.com</span>
  </div>
  <a class="abs quick-contact" href="#">
    <svg width="8" height="8" viewBox="0 0 8 8"><rect x="0.5" y="1.5" width="6" height="6" fill="none" stroke="#fff"/><path d="M3 5 L7.5 0.5" stroke="#fff" stroke-width="1.2"/></svg>
    QUICK CONTACT
  </a>
  <nav>
    <a class="abs main-nav active" style="left:438px" href="#">HOME</a>
    <a class="abs main-nav" style="left:481px" href="#">ABOUT US</a>
    <a class="abs main-nav" style="left:539px" href="#">PORTFOLIO</a>
    <a class="abs main-nav" style="left:601px" href="#">CONTACT</a>
  </nav>
</header>

<section class="abs hero" role="img" aria-label="Blurred close-up photo of source code on a monitor"></section>
<h1 class="abs hero-title">OPEN SOURCE SOFTWARE</h1>
<p class="abs hero-sub">for B2B companies</p>
<a class="abs hero-btn" href="#">Learn More</a>
<svg class="abs hero-arrow" style="left:18px" width="10" height="14" viewBox="0 0 10 14"><path d="M8 1 L2 7 L8 13" stroke="#fff" stroke-width="2.4" fill="none"/></svg>
<svg class="abs hero-arrow" style="left:689px" width="10" height="14" viewBox="0 0 10 14"><path d="M2 1 L8 7 L2 13" stroke="#fff" stroke-width="2.4" fill="none"/></svg>

<section class="abs welcome"></section>
<h2 class="abs section-title" style="top:409px">WELCOME TO K7 SOFTWARE</h2>
<p class="abs welcome-text">Aliquam erat volutpat. Quisque aliquet ex nec est vestibulum pulvinar. Pellentesque convallis molestie enim sit amet efficitur. Etiam id imperdiet lectus. Vivamus lacus justo, ultrices nec erat in, euismod iaculis mauris. Vivamus eleifend vitae nulla vel malesuada. In ac malesuada lacus, et consectetur ante. Fusce vitae lectus sit amet mi pulvinar maximus. Aenean placerat, nibh vel accumsan aliquet, magna nibh accumsan nibh, ac tempus nunc ipsum ac tellus.</p>

<h2 class="abs section-title" style="top:557px">OUR PRODUCTS</h2>
<div class="abs product" style="left:79px;top:587px">
  <div class="product-logo"><span class="product-dot"></span>Bluefox</div>
  <p class="product-name">Blue fox</p>
  <a class="read-more" href="#">Read more</a>
</div>
<div class="abs product" style="left:222px;top:587px">
  <div class="product-logo"><span class="product-dot"></span>Crater</div>
  <p class="product-name">Craters</p>
  <a class="read-more" href="#">Read more</a>
</div>
<div class="abs product" style="left:365px;top:587px">
  <div class="product-logo">Velmor</div>
  <p class="product-name">Velmor</p>
  <a class="read-more" href="#">Read more</a>
</div>
<div class="abs product" style="left:507px;top:587px">
  <div class="product-logo"><span class="product-dot" style="width:44px;height:44px;background:#e2e2e6"></span></div>
  <p class="product-name">Our trust wall</p>
  <a class="read-more" href="#">Read more</a>
</div>

<div class="abs divider"></div>

<h2 class="abs section-title" style="top:775px">BLOG</h2>
<article class="abs post" style="left:79px;top:809px">
  <div class="post-media" role="img" aria-label="Hooded figure in front of blue code screens" style="background:linear-gradient(135deg,#0b3a5a,#145c80 50%,#0a2a40)"></div>
  <div class="post-body">
    <h3 class="post-title">Aliquam consectetur orci moles tie dictum molestie</h3>
    <p class="post-date">16 November 2017</p>
    <p class="post-excerpt">Aenean facilisis tincidunt lectus, id dictum nisi luctus eget. Vivamus efficitur ex condimentum, malesuada eros eget, feugiat nibh. Sed tellus ex, imperdiet eget gravida sit amet, volutpat eget turpis. In nec ultricies est. <span>More</span></p>
  </div>
</article>
<article class="abs post" style="left:271px;top:809px">
  <div class="post-media" role="img" aria-label="Man at a desk working on a laptop in a bright office" style="background:linear-gradient(135deg,#dfe7ef,#9fb3c8 50%,#e9edf1)"></div>
  <div class="post-body">
    <h3 class="post-title">Etiam massa elementum, biben dum tellus venenatis, feugiat</h3>
    <p class="post-date">16 November 2017</p>
    <p class="post-excerpt">Aenean facilisis tincidunt lectus, id dictum nisi luctus eget. Vivamus efficitur ex condimentum, malesuada eros eget, feugiat nibh. Sed tellus ex, imperdiet eget gravida sit amet, volutpat eget turpis. In nec ultricies est. <span>More</span></p>
  </div>
</article>
<article class="abs post" style="left:462px;top:809px">
  <div class="post-media" role="img" aria-label="Hand touching a glowing digital globe over a city at night" style="background:linear-gradient(135deg,#0d2c5a,#2a68a8 55%,#0a1f40)"></div>
  <div class="post-body">
    <h3 class="post-title">Quisque aliquet ex nec est vestib ulum pulvinar</h3>
    <p class="post-date">16 November 2017</p>
    <p class="post-excerpt">Aenean facilisis tincidunt lectus, id dictum nisi luctus eget. Vivamus efficitur ex condimentum, malesuada eros eget, feugiat nibh. Sed tellus ex, imperdiet eget gravida sit amet, volutpat eget turpis. In nec ultricies est. <span>More</span></p>
  </div>
</article>
<a class="abs view-all" href="#">View All</a>

<footer class="abs site-footer"></footer>
<p class="abs footer-nav">Home &nbsp;|&nbsp; About Us &nbsp;|&nbsp; Portfolio &nbsp;|&nbsp; Contact</p>
<p class="abs footer-copy">Copyright &nbsp;©&nbsp; 2017 &nbsp;K7 Software. &nbsp; All rights reserved.</p>
<span class="abs social" style="left:602px;background:#3b5998"></span>
<span class="abs social" style="left:622px;background:#1da1f2"></span>

</body>
</html>
```